Inspire Design with Natural Stone: Quarrelle Inc. Tradeshow Booth Backdrop

Client: Quarrelle Inc.
Project Goal: To design a visually compelling and informative 7.5ft x 10ft backdrop for Quarrelle Inc.'s 10ft x 10ft tradeshow booth that attracts and engages architects, designers, homeowners, and contractors, ultimately driving interest in their natural stone products.
Quarrelle Inc. is a leading provider of high-quality natural stone for a wide range of residential and commercial projects. We offer a diverse selection of stone types, finishes, and applications, known for their beauty, durability, and timeless appeal. We are participating in upcoming tradeshows to generate new leads, strengthen brand awareness, and showcase our latest offerings to key target audiences.
Target Audience(s):
Architects: Seeking premium, unique, and sustainable natural stone options for their designs, with an appreciation for quality and aesthetic integration.
Designers (Interior & Landscape): Looking for visually appealing and versatile stone to enhance their projects, focusing on texture, color palettes, and application possibilities.
Homeowners: Aspiring to elevate their living spaces with natural stone, driven by aesthetics, durability, and adding lasting value to their homes.
Contractors: Seeking reliable and high-quality stone suppliers for their building and renovation projects, prioritizing ease of installation and client satisfaction.
Key Message/Desired Outcome: We want our booth to communicate that Quarrelle Inc. is the premier source for beautiful, high-quality natural stone solutions for any project, backed by expertise and a commitment to customer satisfaction. We want to inspire visitors with the possibilities of using natural stone in their designs and projects.
Mandatories:
* Backdrop Dimensions: 7.5 feet (height) x 10 feet (width). (See attached template)
* Inclusion of Quarrelle Inc. Logo:* The logo must be prominently featured and easily recognizable. Please refer to the attached brand guidelines for logo usage, color palette, and typography.
*Clear Representation of Natural Stone: The design must showcase the beauty and variety of Quarrelle Inc.'s natural stone products. This can be achieved through high-quality photography, subtle textures, or artistic representations. Please use our website's photo and project gallery.
*Contact Information: Include our website address: www.quarrelle-example.com
Optional Elements (Consideration):
*Visuals of Applications: Showcasing natural stone used in various settings (e.g., fireplaces, facades, patios, interior walls) could be impactful.
*Highlighting Key Benefits: Briefly communicating the advantages of natural stone (e.g., durability, sustainability, timelessness).
*Integration of Textures: Subtly incorporating textures that hint at the feel of natural stone.
Look and Feel:
*Overall Impression: Sophisticated, natural, high-quality, inviting, trustworthy, and inspiring.
*Style: Clean, modern, and visually appealing, allowing the beauty of the stone to take center stage. Avoid overly busy or cluttered designs.
*Color Palette: Primarily utilize Quarrelle Inc.'s brand colors (refer to brand guidelines).
Things to Avoid:
* Generic stock imagery that doesn't accurately represent Quarrelle's products.
* Cluttered layouts with excessive text.
* Designs that appear cheap or unprofessional.
* Difficult-to-read fonts or color combinations.
Deliverables:
* High-resolution digital design file(s) suitable for large-format printing (AI, Photoshop, PDF).
* Mockup of the backdrop design within a 10ft x 10ft booth space. Please feel free to include any other booth features (tables, flooring, etc) that you think would work well with the backdrop (optional but highly recommended).
We are excited to see your creative interpretations and look forward to selecting a design that will make a strong and lasting impression at our upcoming tradeshows!

```html
<!DOCTYPE html>
<html lang="en">
<head>
<meta charset="utf-8">
<title>Quarrelle Inc. – Tradeshow Backdrop</title>
<link rel="stylesheet" href="https://fonts.googleapis.com/css2?family=Cinzel:wght@600;700&family=Montserrat:ital,wght@0,500;0,600;0,800;1,800&display=swap">
<style>
  :root {
    --navy: #141c2b;
    --navy-deep: #0d131f;
    --sand: #cbc4aa;
    --sand-dark: #aea68c;
    --sand-text: #d8d0b4;
    --white: #ffffff;
    --ink: #17181c;
    --page: #e9e9e9;
  }
  * { margin: 0; padding: 0; box-sizing: border-box; }
  html, body {
    width: 1200px; height: 960px; overflow: hidden;
    background: var(--page);
  }
  .backdrop {
    position: absolute; left: 0; top: 30px;
    width: 1200px; height: 900px;
    background: radial-gradient(ellipse at 40% 40%, #1c2638 0%, var(--navy) 55%, var(--navy-deep) 100%);
    overflow: hidden;
    font-family: "Montserrat", Arial, sans-serif;
  }
  .backdrop__wave { position: absolute; inset: 0; }
  .brand {
    position: absolute; left: 190px; top: 122px;
    display: flex; align-items: center; gap: 18px;
  }
  .brand__mark { width: 34px; height: 34px; background: var(--sand); }
  .brand__name {
    font-family: "Montserrat", Arial, sans-serif;
    font-weight: 500; font-size: 40px; letter-spacing: 1px;
    color: var(--white);
  }
  .headline {
    position: absolute; left: 190px; top: 250px;
    font-family: "Cinzel", Georgia, serif;
    font-weight: 600; font-size: 46px; line-height: 62px;
    color: var(--sand-text);
  }
  .headline strong { font-weight: 700; color: var(--white); }
  .tagline {
    position: absolute; left: 192px; top: 374px;
    font-weight: 800; font-style: italic; font-size: 15.5px;
    color: var(--white); letter-spacing: 0.2px;
  }
  .services {
    position: absolute; left: 192px; top: 425px;
    list-style: none;
  }
  .services li {
    display: flex; align-items: center; gap: 10px;
    font-weight: 500; font-size: 28px; line-height: 47px;
    color: var(--white);
  }
  .services li::before {
    content: ""; width: 14px; height: 14px; border-radius: 50%;
    background: var(--sand-text);
  }
  .contact { position: absolute; left: 192px; top: 728px; color: var(--ink); }
  .contact__row { display: flex; align-items: center; gap: 14px; }
  .contact__phone { font-weight: 800; font-size: 42px; letter-spacing: 0.5px; }
  .contact__web { font-weight: 500; font-size: 25px; margin-top: 4px; }
  .contact__web b { font-weight: 800; }
  .contact svg { flex: none; }
  .gallery {
    position: absolute; left: 704px; top: 130px;
    display: flex; flex-direction: column; gap: 22px;
  }
  .gallery__photo {
    width: 308px; height: 210px;
    border: 8px solid var(--white);
    box-shadow: 0 4px 10px rgba(0,0,0,0.35);
  }
  .gallery__photo--mill { background: linear-gradient(160deg, #7a3b34 0%, #8e8a82 40%, #6f7b5a 100%); }
  .gallery__photo--house { background: linear-gradient(180deg, #7fa4cf 0%, #c9cacb 45%, #7e8f6a 80%, #a7a59f 100%); }
  .gallery__photo--hearth { background: linear-gradient(180deg, #d9d8d3 0%, #6f6a62 45%, #2f2d2b 65%, #8a8477 100%); }
</style>
</head>
<body>
  <section class="backdrop">
    <svg class="backdrop__wave" viewBox="0 0 1200 900" aria-hidden="true">
      <defs>
        <linearGradient id="sandFill" x1="0" y1="0" x2="1" y2="0">
          <stop offset="0" stop-color="#bdb69c"/>
          <stop offset="0.45" stop-color="#d1cab0"/>
          <stop offset="1" stop-color="#a9a187"/>
        </linearGradient>
      </defs>
      <path d="M0,520 C350,690 800,720 1200,520 L1200,900 L0,900 Z" fill="url(#sandFill)"/>
      <path d="M0,510 C350,680 800,710 1200,510" fill="none" stroke="#ffffff" stroke-width="16"/>
    </svg>

    <div class="brand">
      <span class="brand__mark"></span>
      <span class="brand__name">Quarrelle Inc.</span>
    </div>

    <h1 class="headline">CRAFTING<br>NATURAL <strong>STONE</strong></h1>
    <p class="tagline">FROM SKILLED HANDS TO LASTING BEAUTY</p>

    <ul class="services">
      <li>Stone Veneer</li>
      <li>Hardscape</li>
      <li>Mortar &amp; Tools</li>
    </ul>

    <div class="contact">
      <div class="contact__row">
        <svg width="26" height="26" viewBox="0 0 24 24" aria-hidden="true"><path d="M6.6 10.8a15.1 15.1 0 0 0 6.6 6.6l2.2-2.2c.3-.3.7-.4 1-.2 1.1.4 2.3.6 3.6.6.6 0 1 .4 1 1V20c0 .6-.4 1-1 1A17 17 0 0 1 3 4c0-.6.4-1 1-1h3.5c.6 0 1 .4 1 1 0 1.3.2 2.5.6 3.6.1.3 0 .7-.2 1z" fill="#17181c"/></svg>
        <span class="contact__phone">555-014-2870</span>
      </div>
      <div class="contact__row">
        <svg width="26" height="26" viewBox="0 0 24 24" aria-hidden="true"><circle cx="12" cy="12" r="10" fill="none" stroke="#17181c" stroke-width="2"/><path d="M2 12h20M12 2c3 3 3 17 0 20M12 2c-3 3-3 17 0 20" fill="none" stroke="#17181c" stroke-width="1.6"/></svg>
        <span class="contact__web">www.<b>quarrelle-example</b>.com</span>
      </div>
    </div>

    <div class="gallery">
      <div class="gallery__photo gallery__photo--mill" role="img" aria-label="Photo of a stone-clad mill building with a red waterwheel"></div>
      <div class="gallery__photo gallery__photo--house" role="img" aria-label="Photo of a house with a stone chimney and outdoor stone patio fireplace"></div>
      <div class="gallery__photo gallery__photo--hearth" role="img" aria-label="Photo of an interior stone veneer fireplace with wooden mantel"></div>
    </div>
  </section>
</body>
</html>
```